Brightmark Pixel Collective Website

I need my website redesigned to look very modern with the latest services. Check out my old website for information: www.brightmarkpixelcollective.com

You can use the same site menu links

It doesn't need to have the Recent News section

Please use the yellow, black and grey color scheme

Target Market(s)

25-50 years in range. Small Business Owners

Industry/Entity Type

Group

Requirements
Must have
• Logo and similar color scheme to current website
• Modern, Modern, Modern! I want a very fresh and modern look
Should not have
• Boring Look

```html
<!DOCTYPE html>
<html lang="en">
<head>
<meta charset="utf-8">
<title>Brightmark Pixel Collective</title>
<link href="https://fonts.googleapis.com/css2?family=Open+Sans:wght@300;400;600;700&display=swap" rel="stylesheet">
<style>
:root{
  --yellow:#f7b51b;
  --yellow-dark:#e89a0c;
  --ink:#3a3a3a;
  --slate:#3e4b53;
  --steel:#a4aaae;
  --paper:#f4f4f4;
  --paper-2:#ececec;
  --footer:#3b3b3b;
  --footer-deep:#2a2a2a;
  --muted:#5a5a5a;
  --icon:#3d3d3d;
  --social-1:#3f63a8;
  --social-2:#34a7e0;
  --social-3:#1f7bb6;
  --social-4:#d9412f;
}
*{margin:0;padding:0;box-sizing:border-box}
html,body{width:1077px;height:1200px;overflow:hidden}
body{font-family:"Open Sans",Arial,sans-serif;color:var(--ink);background:#fff;position:relative}
.abs{position:absolute}

/* header */
.site-header{position:absolute;left:0;top:0;width:1077px;height:66px;background:#f7f7f7}
.brand{position:absolute;left:223px;top:19px;display:flex;align-items:center;gap:9px}
.brand-mark{width:26px;height:26px;background:var(--yellow)}
.brand-name{font-weight:300;font-size:16.5px;color:#555;text-transform:uppercase;letter-spacing:.3px;white-space:nowrap}
.phone{position:absolute;left:608px;top:20px;display:flex;gap:8px;align-items:center}
.phone-text{font-size:8.5px;line-height:14px;color:#888;white-space:nowrap}
.phone-text b{color:#222;font-weight:700}
.quote-btn{position:absolute;left:760px;top:19px;width:101px;height:31px;background:linear-gradient(#5a5a5a,#333);border-radius:3px;color:#fff;font-size:9.5px;font-weight:600;text-align:center;line-height:31px;white-space:nowrap}
.quote-btn em{font-style:normal;color:var(--yellow)}

.main-nav{position:absolute;left:0;top:66px;width:1077px;height:30px;background:linear-gradient(var(--yellow),var(--yellow-dark))}
.main-nav span{position:absolute;top:0;line-height:30px;color:#fff;font-size:11px;font-weight:600;text-transform:uppercase}

/* hero */
.hero{position:absolute;left:0;top:96px;width:1077px;height:273px;background:linear-gradient(180deg,#8a8478 0%,#6c6a63 45%,#4f4b44 100%)}
.hero-screen{position:absolute;left:409px;top:20px;width:280px;height:197px;background:linear-gradient(#d9d9d9,#9a9a9a);border-radius:6px}
.hero-screen.side{top:45px;width:210px;height:165px}
.hero-arrow{position:absolute;top:125px;width:30px;height:30px;border-radius:50%}

.tagline{position:absolute;left:0;top:369px;width:1077px;height:70px;background:linear-gradient(#46545c,var(--slate));text-align:center;color:#fff}
.tagline h1{font-size:17px;font-weight:600;margin-top:14px}
.tagline h1 span{color:var(--yellow)}
.tagline p{font-size:12.5px;font-weight:300;color:#e6e6e6}

/* services */
.services{position:absolute;left:0;top:439px;width:1077px;height:122px;background:var(--steel)}
.service{position:absolute;top:18px;width:215px;text-align:center;color:#444}
.service h2{font-weight:300;font-size:16px;margin-top:4px}
.service p{font-size:8.5px;text-transform:uppercase;color:#555}
.divider{position:absolute;top:0;width:1px;height:122px;background:#bfc4c7}

/* recent works */
.works{position:absolute;left:0;top:561px;width:1077px;height:200px;background:var(--paper)}
.works h3{position:absolute;left:223px;top:30px;font-size:11.5px;font-weight:700;text-transform:uppercase}
.works p{position:absolute;left:223px;top:57px;width:150px;font-size:9px;line-height:14px;color:var(--muted)}
.works .pager{position:absolute;left:223px;top:106px;font-size:10px;color:#7a9ab5;letter-spacing:4px}
.work{position:absolute;top:26px;width:148px;height:140px;border:3px solid #fff;box-shadow:0 0 2px #aaa}
.work .thumb{position:absolute;inset:0}
.work .title{position:absolute;left:0;width:100%;bottom:22px;text-align:center;color:#fff;font-weight:300;font-size:12.5px}
.work .cat{position:absolute;left:0;width:100%;bottom:10px;text-align:center;color:#ddd;font-size:7.5px;text-transform:uppercase}
.work.active{border-bottom-color:var(--yellow)}

/* why choose */
.why{position:absolute;left:0;top:761px;width:1077px;height:285px;background:var(--paper-2)}
.why h3{position:absolute;left:0;width:1077px;top:22px;text-align:center;font-weight:400;font-size:16px;color:#555;text-transform:uppercase}
.why .rule{position:absolute;left:223px;top:51px;width:631px;height:1px;background:#d0d0d0}
.feature{position:absolute;width:152px}
.feature .ico{position:absolute;left:0;top:0;width:26px;height:26px;border-radius:50%;background:var(--icon)}
.feature .ico svg{display:block}
.feature h4{position:absolute;left:33px;top:6px;font-size:9.5px;font-weight:700;text-transform:uppercase;white-space:nowrap}
.feature p{position:absolute;left:0;top:35px;width:152px;font-size:8.8px;line-height:13.5px;color:var(--muted)}

/* footer */
.site-footer{position:absolute;left:0;top:1046px;width:1077px;height:122px;background:var(--footer);color:#aaa}
.foot-mark{position:absolute;left:255px;top:24px;width:62px;height:62px;background:var(--yellow)}
.foot-col{position:absolute;top:21px}
.foot-col h5{font-size:9.5px;font-weight:700;color:#eee;margin-bottom:9px}
.foot-col li{list-style:none;font-size:7.5px;line-height:16.2px;color:#999}
.foot-col li::before{content:"›";margin-right:5px;color:#888}
.foot-col li.on{color:var(--yellow)}
.contact-line{font-size:7.5px;line-height:10px;color:#999;display:flex;gap:8px;margin-bottom:10px;white-space:nowrap}
.contact-line svg{flex:none}
.social{display:flex;gap:8px}
.social i{display:block;width:26px;height:23px;border-radius:2px;box-shadow:inset 0 -3px 0 rgba(0,0,0,.2),inset 0 1px 0 rgba(255,255,255,.25)}
.bottom-bar{position:absolute;left:0;top:1168px;width:1077px;height:32px;background:var(--footer-deep);color:#888;font-size:7.5px;line-height:32px}
</style>
</head>
<body>

<header class="site-header">
  <div class="brand"><div class="brand-mark"></div><div class="brand-name">Brightmark Pixel Collective</div></div>
  <div class="phone">
    <svg width="24" height="24" viewBox="0 0 24 24"><circle cx="12" cy="12" r="11" fill="none" stroke="#f7b51b" stroke-width="2"/><path d="M8 7c1-1 2 0 2.5 1.5s-1 1.5-.5 2.5 2 2.5 3 3 1-1 2.5-.5S17 16 16 17c-3 1-9-5-8-10z" fill="#f7b51b"/></svg>
    <div class="phone-text">Local: <b>555-018-2750</b><br>Toll Free: <b>1-800-555-0142</b></div>
  </div>
  <div class="quote-btn">Request <em>FREE</em> Quote</div>
</header>

<nav class="main-nav">
  <span style="left:239px">Home</span>
  <span style="left:328px">Web Design</span>
  <span style="left:453px">Search Engine Marketing</span>
  <span style="left:662px">Social Media</span>
  <span style="left:797px">Contact</span>
</nav>

<section class="hero" role="img" aria-label="Aerial city photograph behind three monitors showing client websites">
  <div class="hero-screen side" style="left:283px"></div>
  <div class="hero-screen side" style="left:600px"></div>
  <div class="hero-screen"></div>
  <svg class="hero-arrow" style="left:184px" viewBox="0 0 30 30"><circle cx="15" cy="15" r="15" fill="#555" opacity=".85"/><path d="M17 10l-5 5 5 5" stroke="#fff" stroke-width="2" fill="none"/></svg>
  <svg class="hero-arrow" style="left:860px" viewBox="0 0 30 30"><circle cx="15" cy="15" r="15" fill="#f7b51b"/><path d="M13 10l5 5-5 5" stroke="#fff" stroke-width="2" fill="none"/></svg>
</section>

<section class="tagline">
  <h1>We are an <span>award winning</span> web design &amp; internet marketing company</h1>
  <p>Suspendisse tristique ante sit amet sem pulvinar posuere.</p>
</section>

<section class="services">
  <div class="service" style="left:216px">
    <svg width="62" height="42" viewBox="0 0 62 42"><rect x="8" y="2" width="46" height="30" rx="2" fill="none" stroke="#444" stroke-width="4"/><path d="M0 36h62l-3 5H3z" fill="#444"/></svg>
    <h2>Web Design</h2><p>It was hard to make it so cool</p>
  </div>
  <div class="divider" style="left:431px"></div>
  <div class="service" style="left:431px">
    <svg width="44" height="46" viewBox="0 0 44 46"><path d="M14 44V36C6 32 4 22 8 14S24 0 32 6s10 18 4 24l-2 3 4 6-6 2v3" fill="none" stroke="#444" stroke-width="2"/><circle cx="22" cy="18" r="6" fill="none" stroke="#444" stroke-width="3"/><circle cx="31" cy="14" r="4" fill="none" stroke="#444" stroke-width="2.5"/></svg>
    <h2>Internet Marketing</h2><p>It was fun to make it so cool</p>
  </div>
  <div class="divider" style="left:646px"></div>
  <div class="service" style="left:646px">
    <svg width="48" height="46" viewBox="0 0 48 46"><circle cx="24" cy="8" r="5" fill="none" stroke="#444" stroke-width="2"/><circle cx="10" cy="22" r="5" fill="#444"/><circle cx="38" cy="22" r="5" fill="#444"/><path d="M2 46v-10c0-6 16-6 16 0v10zM30 46v-10c0-6 16-6 16 0v10z" fill="#444"/></svg>
    <h2>Social Media</h2><p>It is cool to keep it so cool</p>
  </div>
</section>

<section class="works">
  <h3>Recent Works</h3>
  <p>Suspendisse rhoncus facili iscing. Vestibulum eu ligula lorem mus orci sem.</p>
  <div class="pager">‹ ›</div>
  <div class="work" style="left:384px"><div class="thumb" role="img" aria-label="Screenshot of an orange outdoor event website" style="background:linear-gradient(#e3741c,#8e1d12)"></div><div class="title">Project Title</div><div class="cat">Graphic Design</div></div>
  <div class="work active" style="left:546px"><div class="thumb" role="img" aria-label="Screenshot of a green pet care website" style="background:linear-gradient(#5b5a3a,#2e3322)"></div>
    <svg class="abs" style="left:40px;top:50px" width="68" height="28" viewBox="0 0 68 28"><circle cx="14" cy="14" r="13" fill="#fff"/><circle cx="54" cy="14" r="13" fill="#fff"/><path d="M10 18l8-8" stroke="#555" stroke-width="2.5"/><circle cx="52" cy="12" r="5" fill="none" stroke="#555" stroke-width="2"/><path d="M56 16l4 4" stroke="#555" stroke-width="2"/></svg>
    <div class="title">Project Title</div><div class="cat">Graphic Design</div></div>
  <div class="work" style="left:707px"><div class="thumb" role="img" aria-label="Screenshot of a restaurant website with a drink photo" style="background:linear-gradient(#8d9496,#3a2c20)"></div><div class="title">Project Title</div><div class="cat">Graphic Design</div></div>
</section>

<section class="why">
  <h3>Why Choose Us</h3>
  <div class="rule"></div>
  <div class="feature" style="left:223px;top:77px"><div class="ico"><svg width="26" height="26" viewBox="0 0 26 26"><ellipse cx="13" cy="12" rx="6.5" ry="5" fill="#fff"/><path d="M9 15l-2 4 5-3z" fill="#fff"/><path d="M10 12h6" stroke="#3d3d3d" stroke-width="1.2"/></svg></div><h4>Customer Support</h4><p>Select design work for delivery in a beautiful, simple email to clients or teammates.</p></div>
  <div class="feature" style="left:384px;top:77px"><div class="ico"><svg width="26" height="26" viewBox="0 0 26 26"><path d="M7 10V7h3M16 7h3v3M19 16v3h-3M10 19H7v-3" fill="none" stroke="#fff" stroke-width="1.8"/><rect x="10" y="10" width="6" height="6" fill="none" stroke="#fff" stroke-width="1.2"/></svg></div><h4>Responsive</h4><p>Lorem ipsum dolor sit amet, tetur adipiscing elit. Suspendisse smod congue bibendum.</p></div>
  <div class="feature" style="left:546px;top:77px"><div class="ico"><svg width="26" height="26" viewBox="0 0 26 26"><circle cx="13" cy="13" r="7" fill="none" stroke="#fff" stroke-width="1.6"/><ellipse cx="13" cy="13" rx="3" ry="7" fill="none" stroke="#fff" stroke-width="1.2"/><path d="M6 13h14" stroke="#fff" stroke-width="1.2"/></svg></div><h4>Multilanguage</h4><p>Select design work for delivery in a beautiful, simple email to clients or teammates.</p></div>
  <div class="feature" style="left:708px;top:77px"><div class="ico"><svg width="26" height="26" viewBox="0 0 26 26"><path d="M11 6h4M12 6v5l-5 9h12l-5-9V6" fill="none" stroke="#fff" stroke-width="1.5"/><path d="M9 17h8l1.5 3h-11z" fill="#fff"/></svg></div><h4>Web Development</h4><p>Aliquam erat volutpat. Phasellus eget justo lacus. Vivamus pharetra ullamcorper massa.</p></div>
  <div class="feature" style="left:223px;top:174px"><div class="ico"><svg width="26" height="26" viewBox="0 0 26 26"><path d="M8 6h7l4 4v10H8z" fill="none" stroke="#fff" stroke-width="1.6"/><path d="M15 6v4h4M10.5 14h6M10.5 17h6" stroke="#fff" stroke-width="1.2" fill="none"/></svg></div><h4>Well Documented</h4><p>Because we know you don't want to be limited on a portrait or scape format we made Showcase.</p></div>
  <div class="feature" style="left:384px;top:174px"><div class="ico"><svg width="26" height="26" viewBox="0 0 26 26"><path d="M19 6l1 1-8 9-2-2z" fill="#fff"/><path d="M9.5 15l2 2c-1 3-3 3.5-5 3 1-1 1-4 3-5z" fill="#fff"/></svg></div><h4>Unlimited Colors</h4><p>With just a few clicks you can add any color you want.compatible in both portrait AND landscape!</p></div>
  <div class="feature" style="left:546px;top:174px"><div class="ico"><svg width="26" height="26" viewBox="0 0 26 26"><path d="M13 5l8 8-8 8-8-8z" fill="#fff"/><path d="M12 10l-3 3 3 3M14.5 10l3 3-3 3" fill="none" stroke="#3d3d3d" stroke-width="1.4"/></svg></div><h4>HTML5 &amp; CSS3</h4><p>With just a few clicks you can add any color you want.compatible in both portrait AND landscape!</p></div>
  <div class="feature" style="left:708px;top:174px"><div class="ico"><svg width="26" height="26" viewBox="0 0 26 26"><path d="M8.5 7v12M11.5 7v12M14.5 7v12M17.5 7v12" stroke="#fff" stroke-width="1.3"/><rect x="7" y="10" width="3" height="2" fill="#fff"/><rect x="10" y="15" width="3" height="2" fill="#fff"/><rect x="13" y="9" width="3" height="2" fill="#fff"/><rect x="16" y="14" width="3" height="2" fill="#fff"/></svg></div><h4>Customization</h4><p>Aliquam erat volutpat. Phasellus eget justo lacus. Vivamus pharetra ullamcorper massa.</p></div>
</section>

<footer class="site-footer">
  <div class="foot-mark" aria-label="Brightmark Pixel Collective"></div>
  <div class="foot-col" style="left:379px"><h5>Navigation</h5><ul><li>Home</li><li>About</li><li>Services</li><li>Contact</li></ul></div>
  <div class="foot-col" style="left:486px"><h5>Services</h5><ul><li class="on">Web Design</li><li>Graphic Design</li><li>SEO Marketing</li><li>Social MEdia</li></ul></div>
  <div class="foot-col" style="left:594px"><h5>Contact Us</h5>
    <div class="contact-line"><svg width="9" height="10" viewBox="0 0 9 10"><path d="M1 1c1-1 2 0 2.3 1.2s-.8 1.2-.4 2 1.5 2 2.3 2.3.8-.8 2-.4S8.5 8 7.5 9C5 10 0 4 1 1z" fill="#999"/></svg>+1800-123-4567</div>
    <div class="contact-line"><svg width="9" height="10" viewBox="0 0 9 10"><rect x=".5" y="2.5" width="8" height="5.5" fill="none" stroke="#999"/><path d="M.5 2.5l4 3 4-3" fill="none" stroke="#999"/></svg>info@yourwebsite.com</div>
    <div class="contact-line"><svg width="9" height="10" viewBox="0 0 9 10"><path d="M4.5 10L1.3 5A3.3 3.3 0 1 1 7.7 5z" fill="#999"/><circle cx="4.5" cy="3.5" r="1.2" fill="#3b3b3b"/></svg><span>Your Address, Your Country<br><span style="line-height:20px">Your Zip Code</span></span></div>
  </div>
  <div class="foot-col" style="left:740px"><h5>Social</h5><div class="social"><i style="background:var(--social-1)"></i><i style="background:var(--social-2)"></i><i style="background:var(--social-3)"></i><i style="background:var(--social-4)"></i></div></div>
</footer>
<div class="bottom-bar"><span class="abs" style="left:215px">Copyright 2014 © CompanyName - All Rights Reserved</span><span class="abs" style="left:763px">Site Map &nbsp; • &nbsp; Privacy Policy</span></div>

</body>
</html>
```